Physiotherapist for Horse and Rider

I need a web design and a working, functioning website for my profession as physiotherapist. Tabs available for the therapy I offer such a massage, stretching, taping, elektrotherapie en advies. Another tab for introducing myself and one for workshops I want to give. I like a tab for photo's and one for how the clients can contact me.

I like it similar too velorant.be Not too much text to read, a beautifull design with matching colours and nice photo's.

Target Market(s)

horse people

Industry/Entity Type

Massage

Number of Pages Required

1 page

Font styles to use
Serif
Script

Colors
34a6d7
0355a3
0493ce

Requirements
Must have
• I like the blue colours from my logo design.
• Contact with e-mail.
• domain name Paddock Zorg
Nice to have
• some off the photo's I uploaded

```html
<!DOCTYPE html>
<html lang="nl">
<head>
<meta charset="utf-8">
<title>Paddock Zorg – Kinesitherapeut voor paard en ruiter</title>
<link rel="stylesheet" href="https://fonts.googleapis.com/css2?family=Nunito+Sans:wght@400;600;700;800&family=Open+Sans:wght@400;600&display=swap">
<style>
:root{
  --blue-light:#34a6d7;
  --blue-mid:#0493ce;
  --blue-deep:#0355a3;
  --navy:#0a3d8f;
  --nav-bg:#1d1f21;
  --ink:#2b2b2b;
  --muted:#555;
  --grey-band:#e3e3e3;
  --white:#fff;
}
*{margin:0;padding:0;box-sizing:border-box}
html,body{width:1200px;height:3586px;overflow:hidden}
body{position:relative;background:var(--white);font-family:"Open Sans",sans-serif;color:var(--ink)}
.abs{position:absolute}
.heading{font-family:"Nunito Sans",sans-serif;font-weight:700;letter-spacing:.5px}
.photo{position:absolute;overflow:hidden}

/* header */
.site-header{position:absolute;left:0;top:0;width:1200px;height:137px;display:flex;align-items:center;justify-content:center;gap:14px}
.brand-dot{width:22px;height:22px;border-radius:50%;background:var(--blue-mid)}
.brand-name{font-family:"Nunito Sans",sans-serif;font-weight:700;font-size:34px;color:var(--blue-mid)}
.main-nav{position:absolute;left:0;top:137px;width:1200px;height:53px;background:var(--nav-bg);display:flex;justify-content:center}
.main-nav a{display:block;line-height:53px;padding:0 16px;color:var(--white);font-family:"Nunito Sans",sans-serif;font-weight:600;font-size:17px;text-decoration:none}
.main-nav a.active{background:var(--blue-mid)}

/* hero */
.hero{left:0;top:190px;width:1200px;height:565px;background:linear-gradient(90deg,#6b6a5a 0%,#4a4638 35%,#2e2a24 65%,#1e1c19 100%)}
.hero-curve{position:absolute;left:0;top:660px;width:1200px;height:100px}
.hero-title{left:0;top:360px;width:1200px;text-align:center;color:var(--white);font-size:46px;font-weight:800}
.hero-sub{left:0;top:415px;width:1200px;text-align:center;color:var(--white);font-size:30px;font-weight:700}
.btn{display:flex;align-items:center;justify-content:center;font-family:"Nunito Sans",sans-serif;font-weight:700;font-size:16px;text-decoration:none}
.btn-solid{background:var(--blue-mid);color:var(--white)}
.btn-dark{background:var(--blue-deep);color:var(--white)}
.btn-outline{border:2px solid var(--blue-deep);color:var(--blue-deep);background:var(--white)}
.slider-dots{left:555px;top:697px;display:flex;gap:8px}
.slider-dots span{width:13px;height:13px;border-radius:50%;border:2px solid var(--white)}
.slider-dots span.on{background:var(--white)}

/* about */
.section-title{left:0;width:1200px;text-align:center;font-size:30px;color:var(--ink)}
.section-title em{font-style:normal;color:var(--blue-mid)}
.about-text{left:170px;top:842px;width:860px;text-align:center;font-size:14px;line-height:25px;color:var(--muted)}
.about-text p+p{margin-top:14px}

/* treatments blue */
.treat-band{left:0;top:1128px;width:1200px;height:538px;background:linear-gradient(110deg,var(--blue-deep) 0%,#0a6cc0 50%,var(--blue-light) 100%)}
.treat-intro{left:180px;top:1228px;width:840px;text-align:center;color:var(--white);font-size:13.5px;line-height:24px}
.treat-card .caption{position:absolute;left:0;right:0;top:100px;text-align:center;color:var(--white);font-family:"Nunito Sans",sans-serif;font-weight:700;font-size:22px;line-height:30px}
.treat-card .rule{position:absolute;left:120px;right:120px;top:170px;height:2px;background:var(--white)}

/* treatments grey */
.detail-band{left:0;top:1666px;width:1200px;height:502px;background:var(--grey-band)}
.detail-title{left:120px;top:1752px;font-size:30px}
.detail-text{left:120px;top:1806px;width:580px;font-size:12.5px;line-height:21px;color:var(--muted)}
.detail-text p+p{margin-top:12px}
.detail-photo{left:717px;top:1728px;width:368px;height:368px;border-radius:50%;background:radial-gradient(circle at 55% 40%,#5a5048 0%,#3a3430 55%,#2a2522 100%)}

/* workshops */
.title-rule{left:570px;height:2px;width:60px;background:#999}
.workshop-caption{position:absolute;left:0;right:0;bottom:0;height:45px;background:rgba(40,40,40,.75);color:var(--white);font-size:17px;line-height:45px;padding-left:25px}

/* gallery */
.gallery-band{left:0;top:2686px;width:1200px;height:357px;background:var(--grey-band)}

/* contact */
.contact-band{left:0;top:3043px;width:1200px;height:461px;background:linear-gradient(180deg,var(--blue-deep) 0%,#0b5fb0 55%,var(--blue-light) 100%)}
.field{position:absolute;left:117px;width:445px;background:var(--white);font-size:13px;color:#666;padding:8px 12px}
.divider{left:599px;top:3165px;width:2px;height:335px;background:rgba(255,255,255,.55)}
.info-line{position:absolute;left:650px;display:flex;align-items:center;gap:12px;color:var(--white);font-size:16px}
.info-line.indent{left:680px}
.socials{left:650px;top:3318px;display:flex;gap:6px}
.socials span{width:30px;height:30px;border-radius:50%;border:2px solid var(--white)}
.footer{left:0;top:3534px;width:1200px;text-align:center;font-size:14px;color:#333}
</style>
</head>
<body>

<header class="site-header">
  <span class="brand-dot"></span>
  <span class="brand-name">Paddock Zorg</span>
</header>

<nav class="main-nav">
  <a class="active" href="#">HOME</a>
  <a href="#">ABOUT US</a>
  <a href="#">MASSAGE</a>
  <a href="#">STRETCHING</a>
  <a href="#">TAPING</a>
  <a href="#">ELEKTROTHERAPIE EN ADVIES</a>
  <a href="#">PHOTOS</a>
  <a href="#">CONTACT US</a>
</nav>

<section>
  <div class="photo hero abs" role="img" aria-label="Therapeut masseert de hals van een bruin paard in de stal"></div>
  <svg class="hero-curve" viewBox="0 0 1200 100" preserveAspectRatio="none">
    <path d="M0 16 Q600 120 1200 16 L1200 100 L0 100 Z" fill="#fff"/>
  </svg>
  <h1 class="abs heading hero-title">HORSE AND RIDER MASSAGE</h1>
  <p class="abs heading hero-sub">DONEC DICTUM LECTUS NON</p>
  <a class="abs btn btn-solid" href="#" style="left:528px;top:470px;width:146px;height:42px">READ MORE</a>
  <div class="abs slider-dots"><span></span><span class="on"></span><span class="on"></span><span class="on"></span></div>
</section>

<section>
  <h2 class="abs heading section-title" style="top:788px">ABOUT <em>PADDOCK ZORG</em></h2>
  <div class="abs about-text">
    <p>Lotte Verhaeghe, 32 jaar, Paddock Zorg. Lotte studeerde af van de Hogeschool Scheldeland als humaan kinesitherapeut in 2007. Zij begon onmiddellijk aan de opleiding Dierfysiotherapie in de Faculteit Diergeneeskunde te Leuven en studeerde af als Fysiotherapeut voor paarden in 2010. Ze combineert beide als Kinesitherapeut voor Paard en Ruiter.</p>
    <p>Van jaartal tot jaartal schoolde ze zich bij in de Humane Manuele Therapie. In jaartal leerde ze natuurlijk hoefbekappen. Sinds 2016 heeft ze zich ook verdiept in het Manueel Taping Concept en Equitaping.</p>
  </div>
  <a class="abs btn btn-outline" href="#" style="left:528px;top:1033px;width:146px;height:42px">READ MORE</a>
</section>

<section>
  <div class="abs treat-band"></div>
  <h2 class="abs heading section-title" style="top:1180px;color:#fff">BEHANDELINGEN</h2>
  <p class="abs treat-intro">Als mens compenseren we ook vaak kleine ongemakken, waardoor er een onevenwicht ontstaat tussen bepaalde spieren. Dit heeft een effect op ons paard. Voeding is ook zeer belangrijk. Bepaalde voedingsstoffen worden makkelijker opgenomen dan andere. Bij belastende voeding kunnen maagklachten en darmproblemen ontstaan.</p>
  <div class="photo treat-card" role="img" aria-label="Therapeut behandelt een paard in de stal" style="left:160px;top:1338px;width:433px;height:268px;background:linear-gradient(135deg,#6e6a5e,#4a463c 60%,#5c584c)">
    <div class="caption">Maagzuur, lege maag<br>tijdens training</div><div class="rule"></div>
  </div>
  <div class="photo treat-card" role="img" aria-label="Therapeut verzorgt de hoef van een paard" style="left:607px;top:1338px;width:435px;height:268px;background:linear-gradient(135deg,#5a4a3c,#3e3530 60%,#6a7a84)">
    <div class="caption">Tandverzorging,<br>kaakgewicht</div><div class="rule"></div>
  </div>
</section>

<section>
  <div class="abs detail-band"></div>
  <h2 class="abs heading detail-title">BEHANDELINGEN</h2>
  <div class="abs detail-text">
    <p>Massage: heeft als doel de spieren te ontspannen en te versoepelen, de bloeddoorstroming te stimuleren, voedingsstoffen aan en afvalstoffen af te voeren, de vochtcirculatie te verbeteren en mentale rust te geven.</p>
    <p>Stretching: houdt de spieren en de pezen soepel en op lengte. Na een spierscheur wordt het nieuw gevormde litteken- en de collageenweefsel gealigneerd, waardoor deze weefsel veel functioneler kunnen werken. Het bindweefsel wordt sterker en kan grotere krachten aan.</p>
    <p>Elektrotherapie: pijnstillende stroom, genaamd TENS, geeft kleine trillingen in de spiervezels waardoor deze ontspannen. Er komen endorfines vrij. Dit is een lichaamseigen stof die pijnstillend werkt.</p>
  </div>
  <a class="abs btn btn-dark" href="#" style="left:123px;top:2055px;width:148px;height:41px">READ MORE</a>
  <div class="abs detail-photo" role="img" aria-label="Therapeut werkt aan het been van een bont paard"></div>
</section>

<section>
  <h2 class="abs heading section-title" style="top:2202px;color:var(--blue-mid)">WORKSHOPS</h2>
  <div class="abs title-rule" style="top:2252px"></div>
  <div class="photo" role="img" aria-label="Cursist masseert een donker paard" style="left:117px;top:2287px;width:473px;height:325px;background:linear-gradient(135deg,#2a2624,#48423c 55%,#6a665e)">
    <div class="workshop-caption">Zelf je paard masseren</div>
  </div>
  <div class="photo" role="img" aria-label="Therapeut behandelt het been van een bruin paard" style="left:609px;top:2287px;width:474px;height:325px;background:linear-gradient(135deg,#8a8a86,#6a4c34 50%,#a8a8a4)">
    <div class="workshop-caption">Wellnessweekend voor paard en ruiter</div>
  </div>
</section>

<section>
  <div class="abs gallery-band"></div>
  <h2 class="abs heading section-title" style="top:2726px;font-size:27px">PHOTO GALLERY</h2>
  <div class="abs title-rule" style="top:2770px"></div>
  <div class="photo" role="img" aria-label="Paard en therapeut in de stal" style="left:117px;top:2803px;width:230px;height:155px;background:linear-gradient(135deg,#4a4a40,#2a2622)"></div>
  <div class="photo" role="img" aria-label="Therapeut bij een bruin paard" style="left:363px;top:2803px;width:230px;height:155px;background:linear-gradient(135deg,#8a7058,#5a4030)"></div>
  <div class="photo" role="img" aria-label="Therapeut met een paard in de stal" style="left:609px;top:2803px;width:228px;height:155px;background:linear-gradient(135deg,#5a4a3e,#3a2e28)"></div>
  <div class="photo" role="img" aria-label="Therapeut behandelt een donker paard" style="left:853px;top:2803px;width:230px;height:155px;background:linear-gradient(135deg,#5e6a60,#2a2624)"></div>
</section>

<section>
  <div class="abs contact-band"></div>
  <h2 class="abs heading section-title" style="top:3073px;color:#fff">CONTACT US</h2>
  <div class="field" style="top:3167px;height:38px">Name</div>
  <div class="field" style="top:3215px;height:38px">Email address</div>
  <div class="field" style="top:3262px;height:79px">Message</div>
  <a class="abs btn btn-dark" href="#" style="left:117px;top:3353px;width:115px;height:39px;font-size:14px">SUBMIT</a>
  <div class="abs divider"></div>
  <div class="info-line" style="top:3164px">
    <svg width="18" height="22" viewBox="0 0 18 22"><path d="M9 1a7 7 0 0 0-7 7c0 5 7 13 7 13s7-8 7-13a7 7 0 0 0-7-7z" fill="none" stroke="#fff" stroke-width="2"/><circle cx="9" cy="8" r="2.5" fill="#fff"/></svg>
    <span>14 Weidepad Suite B2</span>
  </div>
  <div class="info-line indent" style="top:3202px"><span>Hoeveland, 2470</span></div>
  <div class="info-line" style="top:3236px">
    <svg width="18" height="18" viewBox="0 0 18 18"><path d="M4 1l3 4-2 2c1 3 3 5 6 6l2-2 4 3-2 3C8 17 1 10 1 3z" fill="#fff"/></svg>
    <span>(014) 555-0192</span>
  </div>
  <div class="info-line" style="top:3271px">
    <svg width="18" height="14" viewBox="0 0 18 14"><rect x="1" y="1" width="16" height="12" fill="none" stroke="#fff" stroke-width="2"/><path d="M1 1l8 7 8-7" fill="none" stroke="#fff" stroke-width="2"/></svg>
    <span>info@paddockzorg.be</span>
  </div>
  <div class="abs socials"><span></span><span></span><span></span><span></span></div>
</section>

<footer class="abs footer">© 2017 Company Name &nbsp;All right reserved &nbsp;Term of Use</footer>

</body>
</html>
```